Plumbing Business Letterhead Design

Need a letterhead designed to use for my invoices and letters. I would like it to incorporate my business logo, which i will upload, and use light blue and grey colours. Or any colours that will work well with my logo (im not very good with art to know) . Also the letterhead needs to include the following:
Address - P.O Box 4862 Kellbrook NSW 2563
Email - marcus@tfelwoodplumbing.com.au
ABN - 41 906 572 384
Licence No. - 582064K
Mobile - 0471286540

Plumbing

Sans Serif

```html
<!DOCTYPE html>
<html lang="en">
<head>
<meta charset="utf-8">
<title>Marcus Tfelwood Plumbing – Letterhead</title>
<link rel="stylesheet" href="https://fonts.googleapis.com/css2?family=Open+Sans:wght@400;600&display=swap">
<style>
  :root {
    --paper: #ffffff;
    --ink-grey: #5a5b5d;
    --text-grey: #6d6e71;
    --accent-orange: #f7941d;
    --accent-blue: #29a8e0;
  }
  html, body {
    margin: 0;
    padding: 0;
    overflow: hidden;
    background: var(--paper);
  }
  .letterhead {
    position: relative;
    width: 922px;
    height: 1200px;
    background: var(--paper);
    font-family: "Open Sans", Arial, sans-serif;
    overflow: hidden;
  }
  .brand {
    position: absolute;
    left: 54px;
    top: 64px;
    display: flex;
    align-items: center;
    gap: 12px;
  }
  .brand-mark {
    width: 54px;
    height: 54px;
    border-radius: 50%;
    background: var(--accent-blue);
    flex: none;
  }
  .brand-name {
    margin: 0;
    color: var(--ink-grey);
    font-size: 22px;
    font-weight: 600;
    line-height: 26px;
    letter-spacing: 0.2px;
  }
  .contact {
    position: absolute;
    left: 546px;
    top: 72px;
    margin: 0;
    font-size: 14.6px;
    line-height: 21.5px;
    color: var(--text-grey);
    font-style: normal;
  }
  .contact-line { display: block; white-space: nowrap; }
  .label-orange { color: var(--accent-orange); }
  .label-blue { color: var(--accent-blue); }
  .divider { padding: 0 6px; }
  .footer-band {
    position: absolute;
    left: 0;
    top: 1186px;
    width: 922px;
    height: 11px;
    display: block;
  }
</style>
</head>
<body>
  <div class="letterhead">
    <header class="brand">
      <span class="brand-mark" aria-hidden="true"></span>
      <p class="brand-name">Marcus<br>Tfelwood<br>Plumbing</p>
    </header>

    <address class="contact">
      <span class="contact-line"><span class="label-orange">ABN -</span> 41 906 572 384<span class="divider">|</span><span class="label-blue">Licence No.</span> - 582064K</span>
      <span class="contact-line"><span class="label-orange">Email -</span> marcus@tfelwoodplumbing.com.au</span>
      <span class="contact-line"><span class="label-orange">Address -</span> P.O Box 4862 Kellbrook NSW 2563</span>
    </address>

    <svg class="footer-band" viewBox="0 0 922 11" aria-hidden="true">
      <polygon points="0,0 466,0 457,11 0,11" fill="var(--accent-orange)"/>
      <polygon points="471,0 922,0 922,11 462,11" fill="var(--accent-blue)"/>
    </svg>
  </div>
</body>
</html>
```